Indie Record Label Seeking Website Redesign For Synthpop Duo

LA indie label looking for a redesign of the website for our 80s influenced synthpop duo Lantern Orchard. Musical influences include Velour Signal, The Harbins, Clocks Of Glass, Tin Kite Girls, Grey Tundra. More current influences would be Dunes & Dunes, Bo Vell, Glyndrax, Marble Cove. The website is lanternorchard.com. Current sections include the following: News, Bio, Music, Video, Gallery and Contact. We would like to add a "Store" section as well. The redesign should be clean, modern and simple. It should be similar in look and feel to the attached cover of the band's upcoming debut album release entitled Silver Weather. Also attached are the band's logo and photo. We look forward to your submissions!

Dovetail Records

```html
<!DOCTYPE html>
<html lang="en">
<head>
<meta charset="utf-8">
<title>Lantern Orchard — Official Site</title>
<link rel="stylesheet" href="https://fonts.googleapis.com/css2?family=Roboto:wght@300;400;500;700&display=swap">
<style>
:root{
  --bg:#1b1b1b;
  --header:#202020;
  --hero-a:#3a3a3a;
  --hero-b:#151515;
  --section:#1d1d1d;
  --news:#0d0d0d;
  --avail:#2b2b2b;
  --footer:#181818;
  --text:#f2f2f2;
  --muted:#9a9a9a;
  --dim:#6d6d6d;
  --accent:#d8a25a;
  --line:#333;
}
*{margin:0;padding:0;box-sizing:border-box}
html,body{width:835px;height:1200px;overflow:hidden}
body{background:var(--bg);color:var(--text);font-family:'Roboto',Arial,sans-serif}
.page{width:835px;height:1200px;display:flex;flex-direction:column}

.site-header{height:45px;background:var(--header);display:flex;align-items:center;justify-content:space-between;padding:0 70px 0 72px}
.brand{display:flex;align-items:center;gap:9px;font-size:17px;font-weight:400;color:var(--text)}
.brand-mark{width:22px;height:22px;border-radius:50%;background:var(--accent)}
.main-nav{display:flex;gap:22px;font-size:10px;color:var(--muted)}
.main-nav a{color:inherit;text-decoration:none}
.main-nav a.active{color:var(--text)}

.hero{height:310px;position:relative;background:linear-gradient(100deg,var(--hero-a) 0%,#2a2a2a 45%,var(--hero-b) 100%);overflow:hidden}
.hero-copy{position:absolute;left:72px;top:70px;width:300px}
.hero-copy h1{font-size:25px;font-weight:300;line-height:1.2;margin-bottom:14px}
.hero-copy p{font-size:8.5px;line-height:1.6;color:var(--muted)}
.hero-photo{position:absolute;left:440px;top:0;width:230px;height:310px;background:radial-gradient(ellipse at 55% 40%,#d9d9d9 0%,#8a8a8a 35%,#2a2a2a 70%,transparent 100%)}
.hero-arrow{position:absolute;top:140px;width:16px;height:28px;background:#2e2e2e;display:flex;align-items:center;justify-content:center}
.hero-arrow.prev{left:0}.hero-arrow.next{right:0}

.featured{background:var(--section);height:415px;padding-top:42px}
.section-title{text-align:center;font-size:17px;font-weight:300;margin-bottom:22px}
.media-grid{display:grid;grid-template-columns:repeat(6,100px);column-gap:19px;row-gap:18px;justify-content:center}
.media-thumb{width:100px;height:88px;position:relative;display:flex;align-items:center;justify-content:center}
.play{width:24px;height:24px}
.media-caption{margin-top:6px;font-size:7px;line-height:1.45}
.media-caption .title{color:var(--text)}
.media-caption .sub{color:var(--dim)}

.news{background:var(--news);height:120px;padding:14px 70px 0}
.news-head{display:flex;justify-content:space-between;align-items:center;margin-bottom:10px}
.news-head h2{font-size:14px;font-weight:400}
.news-dot{width:7px;height:7px;border-radius:50%;background:#ddd}
.news-row{display:flex;gap:14px;align-items:flex-start}
.news-image{width:130px;height:70px;flex:none}
.news-text{width:185px;font-size:6.5px;line-height:1.5;color:var(--dim)}
.news-text h3{font-size:6.5px;font-weight:500;color:var(--text);margin-bottom:3px}

.available{background:var(--avail);height:160px;text-align:center;padding-top:30px}
.available h2{font-size:19px;font-weight:300;margin-bottom:8px}
.available p{font-size:7.5px;color:var(--muted);margin-bottom:18px}
.actions{display:flex;justify-content:center;gap:14px}
.btn{height:34px;border:1px solid #555;background:#1e1e1e;color:var(--text);font-size:8px;display:flex;align-items:center;justify-content:center;gap:7px;padding:0 14px;min-width:84px}
.btn.store{min-width:100px;text-align:left;line-height:1.2}
.btn-icon{width:12px;height:12px;background:#cfcfcf}

.site-footer{background:var(--footer);flex:1;text-align:center;padding-top:22px}
.footer-nav{display:flex;justify-content:center;gap:14px;font-size:7.5px;color:var(--muted);margin-bottom:9px}
.copyright{font-size:6.5px;color:var(--dim);margin-bottom:14px}
.social{display:flex;justify-content:center;gap:10px}
.social span{width:11px;height:11px;border-radius:50%;background:#6a6a6a}
</style>
</head>
<body>
<div class="page">

  <header class="site-header">
    <div class="brand"><span class="brand-mark"></span>Lantern Orchard</div>
    <nav class="main-nav">
      <a class="active">Home</a><a>Bio</a><a>Music</a><a>Video</a><a>Gallery</a><a>Store</a><a>Contact</a>
    </nav>
  </header>

  <section class="hero">
    <div class="hero-copy">
      <h1>Welcome to<br>Lantern Orchard</h1>
      <p>Lantern Orchard is a synthpop duo from Los Angeles, blending glassy eighties textures with modern pulse. Their debut album Silver Weather arrives soon, carrying bright hooks, warm analog drums and late night melodies for dreamers everywhere.</p>
    </div>
    <div class="hero-photo" role="img" aria-label="Black and white portrait of a band member"></div>
    <div class="hero-arrow prev"><svg width="6" height="10" viewBox="0 0 6 10"><path d="M5 1 1 5l4 4" fill="none" stroke="#aaa" stroke-width="1.4"/></svg></div>
    <div class="hero-arrow next"><svg width="6" height="10" viewBox="0 0 6 10"><path d="M1 1l4 4-4 4" fill="none" stroke="#aaa" stroke-width="1.4"/></svg></div>
  </section>

  <section class="featured">
    <h2 class="section-title">Check out our Featured Musics and Videos</h2>
    <div class="media-grid">
      <div><div class="media-thumb" role="img" aria-label="Album cover artwork" style="background:linear-gradient(135deg,#c95a2c,#3d2a22)"><svg class="play" viewBox="0 0 24 24"><circle cx="12" cy="12" r="11" fill="rgba(0,0,0,.45)" stroke="#fff"/><path d="M10 7.5v9l7-4.5z" fill="#fff"/></svg></div><div class="media-caption"><div class="title">Lantern Orchard</div><div class="sub">Welcome to Lantern Orchard</div></div></div>
      <div><div class="media-thumb" role="img" aria-label="Album cover artwork" style="background:linear-gradient(135deg,#e8e2d6,#8f8a80)"><svg class="play" viewBox="0 0 24 24"><circle cx="12" cy="12" r="11" fill="rgba(0,0,0,.45)" stroke="#fff"/><path d="M10 7.5v9l7-4.5z" fill="#fff"/></svg></div><div class="media-caption"><div class="title">Lantern Orchard</div><div class="sub">Welcome to Lantern Orchard</div></div></div>
      <div><div class="media-thumb" role="img" aria-label="Album cover artwork" style="background:linear-gradient(135deg,#a88a62,#4a3a2a)"><svg class="play" viewBox="0 0 24 24"><circle cx="12" cy="12" r="11" fill="rgba(0,0,0,.45)" stroke="#fff"/><path d="M10 7.5v9l7-4.5z" fill="#fff"/></svg></div><div class="media-caption"><div class="title">Lantern Orchard</div><div class="sub">Welcome to Lantern Orchard</div></div></div>
      <div><div class="media-thumb" role="img" aria-label="Band photo cover" style="background:linear-gradient(135deg,#b9b9b9,#4b4b4b)"><svg class="play" viewBox="0 0 24 24"><circle cx="12" cy="12" r="11" fill="rgba(0,0,0,.45)" stroke="#fff"/><path d="M10 7.5v9l7-4.5z" fill="#fff"/></svg></div><div class="media-caption"><div class="title">Lantern Orchard</div><div class="sub">Welcome to Lantern Orchard</div></div></div>
      <div><div class="media-thumb" role="img" aria-label="Concert video still" style="background:linear-gradient(135deg,#4d7fa3,#1d2a3a)"><svg class="play" viewBox="0 0 24 24"><circle cx="12" cy="12" r="11" fill="rgba(0,0,0,.45)" stroke="#fff"/><path d="M10 7.5v9l7-4.5z" fill="#fff"/></svg></div><div class="media-caption"><div class="title">Lantern Orchard</div><div class="sub">Welcome to Lantern Orchard</div></div></div>
      <div><div class="media-thumb" role="img" aria-label="Band portrait" style="background:linear-gradient(135deg,#6f8fb0,#2c3340)"><svg class="play" viewBox="0 0 24 24"><circle cx="12" cy="12" r="11" fill="rgba(0,0,0,.45)" stroke="#fff"/><path d="M10 7.5v9l7-4.5z" fill="#fff"/></svg></div><div class="media-caption"><div class="title">Lantern Orchard</div><div class="sub">Welcome to Lantern Orchard</div></div></div>

      <div><div class="media-thumb" role="img" aria-label="Album cover artwork" style="background:linear-gradient(135deg,#c4367a,#2a1030)"><svg class="play" viewBox="0 0 24 24"><circle cx="12" cy="12" r="11" fill="rgba(0,0,0,.45)" stroke="#fff"/><path d="M10 7.5v9l7-4.5z" fill="#fff"/></svg></div><div class="media-caption"><div class="title">Lantern Orchard</div><div class="sub">Welcome to Lantern Orchard</div></div></div>
      <div><div class="media-thumb" role="img" aria-label="Album cover artwork" style="background:linear-gradient(135deg,#7a2b24,#151515)"><svg class="play" viewBox="0 0 24 24"><circle cx="12" cy="12" r="11" fill="rgba(0,0,0,.45)" stroke="#fff"/><path d="M10 7.5v9l7-4.5z" fill="#fff"/></svg></div><div class="media-caption"><div class="title">Lantern Orchard</div><div class="sub">Welcome to Lantern Orchard</div></div></div>
      <div><div class="media-thumb" role="img" aria-label="Album cover artwork" style="background:linear-gradient(135deg,#d87a3a,#5a3a6a)"><svg class="play" viewBox="0 0 24 24"><circle cx="12" cy="12" r="11" fill="rgba(0,0,0,.45)" stroke="#fff"/><path d="M10 7.5v9l7-4.5z" fill="#fff"/></svg></div><div class="media-caption"><div class="title">Lantern Orchard</div><div class="sub">Welcome to Lantern Orchard</div></div></div>
      <div><div class="media-thumb" role="img" aria-label="Album cover artwork" style="background:linear-gradient(135deg,#3a7ab0,#c77a3a)"><svg class="play" viewBox="0 0 24 24"><circle cx="12" cy="12" r="11" fill="rgba(0,0,0,.45)" stroke="#fff"/><path d="M10 7.5v9l7-4.5z" fill="#fff"/></svg></div><div class="media-caption"><div class="title">Lantern Orchard</div><div class="sub">Welcome to Lantern Orchard</div></div></div>
      <div><div class="media-thumb" role="img" aria-label="Band photo" style="background:linear-gradient(135deg,#9a9a8a,#3a3a32)"><svg class="play" viewBox="0 0 24 24"><circle cx="12" cy="12" r="11" fill="rgba(0,0,0,.45)" stroke="#fff"/><path d="M10 7.5v9l7-4.5z" fill="#fff"/></svg></div><div class="media-caption"><div class="title">Lantern Orchard</div><div class="sub">Welcome to Lantern Orchard</div></div></div>
      <div><div class="media-thumb" role="img" aria-label="Live performance still" style="background:linear-gradient(135deg,#5a6a7a,#1a1e24)"><svg class="play" viewBox="0 0 24 24"><circle cx="12" cy="12" r="11" fill="rgba(0,0,0,.45)" stroke="#fff"/><path d="M10 7.5v9l7-4.5z" fill="#fff"/></svg></div><div class="media-caption"><div class="title">Lantern Orchard</div><div class="sub">Welcome to Lantern Orchard</div></div></div>
    </div>
  </section>

  <section class="news">
    <div class="news-head"><h2>Latest News</h2><span class="news-dot"></span></div>
    <div class="news-row">
      <div class="news-image" role="img" aria-label="News photo of the duo" style="background:linear-gradient(135deg,#b03040,#2a1a20)"></div>
      <div class="news-text"><h3>TOUR DATES ANNOUNCED FOR THE SILVER WEATHER SPRING RUN — AUGUST 11, 2015</h3>The duo will play twelve cities this spring, with new visuals and songs from the debut record on the setlist.</div>
      <div class="news-image" role="img" aria-label="News article screenshot" style="background:linear-gradient(135deg,#e8e8e8,#9a9a9a)"></div>
      <div class="news-text"><h3>TOUR DATES ANNOUNCED FOR THE SILVER WEATHER SPRING RUN — AUGUST 11, 2015</h3>The duo will play twelve cities this spring, with new visuals and songs from the debut record on the setlist.</div>
    </div>
  </section>

  <section class="available">
    <h2>Available Now!</h2>
    <p>Stream and download the new single Silver Weather now on your favourite platform.</p>
    <div class="actions">
      <div class="btn store"><span class="btn-icon"></span><span>Download on the<br>Tunebay Store</span></div>
      <div class="btn">Register Now</div>
      <div class="btn">Login</div>
    </div>
  </section>

  <footer class="site-footer">
    <nav class="footer-nav"><span>Home</span><span>Bio</span><span>Music</span><span>Gallery</span><span>Store</span><span>Contact</span></nav>
    <div class="copyright">Copyright © 2015 Lantern Orchard · All rights reserved</div>
    <div class="social"><span></span><span></span><span></span><span></span></div>
  </footer>

</div>
</body>
</html>
```